Music Festival in Colorado Needs Awesome Flier Design

We need an eye-catching & captivating flier design for an annual music festival in Denver, CO (USA). The festival features the best Colorado musicians within the genres of jam - funk - bluegrass - electronic - reggae - rock.

The design should look clean and professional while still being creative and unique. The past three years' flier designs are attached, as well as the logo and some other designs that match the aesthetic of what we're looking for.

This festival has a big element of Colorado pride so any

Target Market(s)

Hippies - live music enthusiasts - partiers. Ages 21 - 40.

Industry/Entity Type

Entertainment

Colors
0355a3
ec1f27
ffffff
fbed22

Requirements
Must have
• Attached design text.
Nice to have
• - Quality texture and psychedelic elements.
• - Colorado pride elements; color scheme (red, white, blue & yellow), flag, ect.
• - Nature elements are awesome but this is also a downtown festival so keep that in mind.
Should not have
• Cheesy artwork.

```html
<!DOCTYPE html>
<html lang="en">
<head>
<meta charset="utf-8">
<title>Pass the Sound – Colorado Music Festival 2018</title>
<link rel="stylesheet" href="https://fonts.googleapis.com/css2?family=Open+Sans:wght@700&family=Oswald:wght@500;700&family=Source+Sans+3:wght@600&display=swap">
<style>
  :root {
    --sky-top: #b9ecdd;
    --sky-mid: #9fe6d4;
    --sky-low: #c8f0e6;
    --gold: #d9b21a;
    --brand: #7a3222;
    --ink: #111111;
    --lineup: #a11c24;
    --peak: #b86a4a;
    --dusk: #e39a5a;
    --city: #3b3f4a;
    --meadow: #4f9a2a;
  }
  html, body { margin: 0; padding: 0; overflow: hidden; }
  body { width: 777px; height: 1200px; background: var(--sky-mid); }
  .flier {
    position: relative;
    width: 777px;
    height: 1200px;
    overflow: hidden;
    background:
      radial-gradient(ellipse at 50% 35%, rgba(255,255,255,0.35), transparent 60%),
      linear-gradient(180deg, var(--sky-top) 0%, var(--sky-mid) 45%, var(--sky-low) 75%);
    text-align: center;
  }
  .landscape {
    position: absolute;
    left: 0; right: 0; bottom: 0;
    height: 430px;
    background:
      linear-gradient(180deg, rgba(200,240,230,0) 0%, rgba(227,154,90,0.45) 28%, var(--peak) 48%, var(--city) 70%, var(--meadow) 86%, #3d7f1e 100%);
  }
  .edition {
    position: absolute;
    top: 50px; left: 0; right: 0;
    font-family: "Open Sans", sans-serif;
    font-weight: 700;
    font-size: 30px;
    line-height: 40px;
    color: var(--gold);
    margin: 0;
  }
  .brand {
    position: absolute;
    top: 138px; left: 0; right: 0;
    font-family: "Oswald", sans-serif;
    font-weight: 700;
    color: var(--brand);
    margin: 0;
    line-height: 1;
  }
  .brand .lead { display: block; font-size: 50px; letter-spacing: 1px; }
  .brand .main { display: block; font-size: 170px; letter-spacing: -2px; margin-top: -4px; }
  .brand .tag { display: block; font-size: 26px; letter-spacing: 3px; margin-top: 8px; }
  .genres {
    position: absolute;
    top: 435px; left: 0; right: 0;
    font-family: "Oswald", sans-serif;
    font-weight: 500;
    font-size: 30px;
    letter-spacing: -0.5px;
    color: var(--ink);
    margin: 0;
  }
  .lineup {
    position: absolute;
    top: 490px; left: 0; right: 0;
    margin: 0; padding: 0;
    list-style: none;
    font-family: "Source Sans 3", sans-serif;
    font-weight: 600;
    font-size: 21px;
    line-height: 28.4px;
    color: var(--lineup);
  }
  .lineup li { white-space: nowrap; }
</style>
</head>
<body>
<main class="flier">
  <div class="landscape" role="img" aria-label="Illustration of Colorado mountain peaks at sunset above the Denver skyline with yellow wildflowers and grass in the foreground"></div>

  <p class="edition">6TH ANNUAL<br>MAY 11TH - 13TH, 2018</p>

  <h1 class="brand">
    <span class="lead">PASS THE</span>
    <span class="main">SOUND</span>
    <span class="tag">COLORADO MUSIC FESTIVAL</span>
  </h1>

  <p class="genres">JAM • FUNK • BLUEGRASS • ELECTRONIC • REGGAE • ROCK</p>

  <ul class="lineup">
    <li>JESS ALDEN BAND • EVERYBODY ORCHESTRA • BRAKE THEORY •</li>
    <li>THE LUCKY SEEDS • J-ROW &amp; THE SUMMIT • DEADTROUT</li>
    <li>ORCHESTRA • KODIAKA • DYNOTRACKER • WILDWATER</li>
    <li>RAMBLE • ELEVATION ENSEMBLE • ANALOG SUN • THE GRAND</li>
    <li>RANCH • SKYTONED • EVERHOFF • KINETICS • POLYFOREST •</li>
    <li>CABLE JUNCTION • METASONICS • SPECTRALE • LUCID MOTION •</li>
    <li>CABLE JUNCTION, LOOPS • THE SWEET POPPIES • JOVIO CLUB •</li>
    <li>JALEN CORBIN BAND • ATOMIKA • ROOTSASAURUS • TRNDLE •</li>
    <li>OTHER BLUE • THE IDLEWAYS • MAMA JUNIPER • TENTH</li>
    <li>PEAK DIVISION • AMORALUNA • ENVY ODA • BOOGIE</li>
    <li>MASTODON • CASUAL CAPTAIN • MIKEY LIGHTNING •</li>
    <li>WAHKONISET • PROJECT 528 • APEX WAVE • COLLIDORAMA •</li>
    <li>CASSIE RUSSO &amp; THE SOUL CABIN • LOLA ASCENDING • TENTH</li>
    <li>PEAK DIVISION • MSITU</li>
  </ul>
</main>
</body>
</html>
```